Innovative global company needs a design for an attractive customer business quote

We need a design for a business quote which is a written offer from a seller to a prospective buyer. Business quotes are often a key step in the complex sales process.

Our company brings human insight to business by studying how people work, wherever they work. Those insights can help organizations achieve a higher level of performance, by creating places that unlock the promise of their people. We are a global, publicly traded company.

Guidelines:
Version 1: Use all the data from the example to product an attractive looking quote using every bit of detail. It should clearly explain to a customer what there order will look like.
Version 2: Use a subset of the data (highlighted on second document) to product a leaner/cleaner looking quote.

• All versions need to use the product illustrations for a quick visual reference to the reader (in zip file, image files named by catalog number).
• The output should be scalable to US Letter and European A4
• The quote should look professional but not stuffy.
• Color is OK to use (no red)
• Make sure you leave space for a logo, along with company information.
• Should be light and airy with white space
Updates

The design needs to be creative and unique. We are ok with it being drastically different as long as it has the content.

I want 2 versions, one with all the data and the other with just the text highlighted in yellow.
I want this quote to be readable and easy for customers to understand.
the vertical lines are not required, in fact it would be nice to see a design without those vertical lines

Industry/Entity Type

Business

Font styles to use
Sans Serif

Requirements
Must have
• 2 versions submitted:
One is with all the data
Second is the subset of the data (note the highlighted text).

Both version must have Art.

```html
<!DOCTYPE html>
<html lang="en">
<head>
<meta charset="utf-8">
<title>Quotation 2327</title>
<link rel="stylesheet" href="https://fonts.googleapis.com/css2?family=Questrial&family=Bitter:wght@400;600&family=Arimo:wght@400;700&display=swap">
<style>
  :root {
    --ink: #3a3a3a;
    --muted: #555;
    --brand: #2c2b8f;
    --band-text: #ffffff;
    --rule: #c9c9c9;
    --frame: #4a4a4a;
    --paper: #ffffff;
    --desk-tone: #7d8286;
    --tower-tone: #dcdcdc;
  }
  * { box-sizing: border-box; margin: 0; padding: 0; }
  html, body { width: 952px; height: 1200px; overflow: hidden; background: var(--paper); }
  body { position: relative; font-family: "Arimo", Arial, sans-serif; color: var(--ink); font-size: 13px; line-height: 15.4px; }

  .sheet {
    position: absolute; left: 53px; top: 53px; width: 846px; height: 1095px;
    background: var(--paper); border: 1px solid var(--frame);
    box-shadow: 3px 4px 10px rgba(0,0,0,.35);
  }
  .abs { position: absolute; }
  .title { right: 48px; top: 40px; font-family: "Questrial", sans-serif; font-size: 37px; line-height: 40px; color: var(--brand); }

  .band { left: 0; width: 844px; background: var(--brand); color: var(--band-text);
    font-family: "Bitter", serif; font-size: 10.5px; line-height: 11px; text-transform: uppercase; }
  .band-meta { top: 172px; height: 37px; }
  .band-items { top: 391px; height: 37px; }
  .band .cell { position: absolute; top: 50%; transform: translate(-50%, -50%); text-align: center; white-space: nowrap; }

  .meta-values { top: 209px; left: 0; width: 844px; height: 38px; border-bottom: 1px solid var(--rule); }
  .meta-values .v { position: absolute; top: 12px; transform: translateX(-50%); white-space: nowrap; }
  .meta-values .v.left { transform: none; }

  .party-label { font-family: "Bitter", serif; font-weight: 600; font-size: 16px; color: var(--brand); line-height: 20px; }
  .party { font-size: 15px; line-height: 18.5px; color: var(--muted); }
  .party strong { font-weight: 700; color: var(--ink); }

  .line-item { left: 0; width: 844px; }
  .line-item .num { position: absolute; transform: translateX(-50%); color: var(--muted); }
  .line-item .price { position: absolute; text-align: right; color: var(--muted); }
  .spec { position: absolute; left: 210px; width: 360px; }
  .spec .model { font-weight: 700; }
  .spec .brand { position: absolute; left: 141px; top: 0; font-weight: 700; }
  .spec .desc { font-weight: 700; }
  .attr { display: grid; grid-template-columns: 52px auto; }
  .options-head { font-weight: 700; margin-top: 4px; }
  .opt { display: grid; grid-template-columns: 141px auto; margin-top: 5px; }
  .opt .key { padding-left: 12px; }
  .opt .key span { display: block; padding-left: 10px; }
  .opt .key span:first-child { padding-left: 0; }
  .opt .key span:first-child::before { content: "•"; margin-right: 5px; }
  .opt .val span { display: block; padding-left: 12px; }
  .opt .val span:first-child { padding-left: 0; }
  .item-rule { position: absolute; left: 0; width: 844px; border-top: 1px solid var(--rule); }

  .art { position: absolute; }
  .art-desk { background: var(--desk-tone); border-radius: 2px; }
  .art-tower { background: linear-gradient(180deg, #ececec, var(--tower-tone)); border: 1px solid #c4c4c4; }
</style>
</head>
<body>
<main class="sheet">
  <h1 class="abs title">Quotation</h1>

  <div class="abs band band-meta">
    <div class="cell" style="left:72px">Quote<br>Number</div>
    <div class="cell" style="left:198px">Quote<br>Date</div>
    <div class="cell" style="left:340px">Customer<br>Order Number</div>
    <div class="cell" style="left:478px">Customer<br>Number</div>
    <div class="cell" style="left:625px">Account<br>Representative</div>
    <div class="cell" style="left:790px">Project<br>ID</div>
  </div>
  <div class="abs meta-values">
    <span class="v" style="left:72px">2327</span>
    <span class="v" style="left:198px">4/10/2014</span>
    <span class="v" style="left:340px">1467942</span>
    <span class="v" style="left:478px">35</span>
    <span class="v left" style="left:592px">Dan Holloway</span>
    <span class="v" style="left:790px">abc1</span>
  </div>

  <div class="abs party-label" style="left:40px; top:284px">QUOTE TO:</div>
  <div class="abs party" style="left:159px; top:284px"><strong>Larkfield Company</strong><br>2210 Lakeview Avenue<br>Fairhaven, MI 49600</div>
  <div class="abs party-label" style="left:497px; top:284px">SHIP TO:</div>
  <div class="abs party" style="left:604px; top:284px"><strong>Larkfield Company</strong><br>2210 Lakeview Avenue<br>Fairhaven, MI 49600</div>

  <div class="abs band band-items">
    <div class="cell" style="left:57px">Line</div>
    <div class="cell" style="left:155px">Quantity</div>
    <div class="cell" style="left:416px">Model Number / Description</div>
    <div class="cell" style="left:684px">Unit<br>Price</div>
    <div class="cell" style="left:790px">Extended<br>Amount</div>
  </div>

  <section class="abs line-item" style="top:438px">
    <span class="num" style="left:57px">1</span>
    <span class="num" style="left:155px">5</span>
    <div class="spec">
      <div class="model">MR7UC2436</div><span class="brand">Northvale</span>
      <div class="desc">Meridian Freestanding; Desk-Corner</div>
      <div class="desc">24D x 36W</div>
      <div class="attr"><span>Basic</span><span>: 4606 Mist</span></div>
      <div class="attr"><span>Edge</span><span>: 6000 Black</span></div>
      <div class="attr"><span>Top-Surf</span><span>: 2746 Black</span></div>
      <div class="options-head">Options:</div>
      <div class="opt"><div class="key"><span>Wksf Opt</span><span>Scallop</span></div><div class="val"><span>*Opt: Worksurface Option</span><span>Scallop</span></div></div>
      <div class="opt"><div class="key"><span>Supt Opt</span><span>3 Corner</span></div><div class="val"><span>*Opt: Support Options</span><span>Std: 3 Corner Supports</span></div></div>
      <div class="opt"><div class="key"><span>Mod Pnl</span><span>Half Mod</span></div><div class="val"><span>*Opt: Modesty Panel Options</span><span>Half Height Modesty Panel</span></div></div>
    </div>
    <div class="art art-desk" role="img" aria-label="Product illustration: corner desk with dark worksurface" style="left:559px; top:5px; width:64px; height:28px"></div>
    <span class="price" style="left:620px; width:102px">$850.00</span>
    <span class="price" style="left:720px; width:108px">$850.00</span>
  </section>

  <div class="item-rule" style="top:675px"></div>

  <section class="abs line-item" style="top:696px">
    <span class="num" style="left:57px">2</span>
    <span class="num" style="left:155px">2</span>
    <div class="spec">
      <div class="model">K6TW241572E</div><span class="brand">Northvale</span>
      <div class="desc">Tower, Door hinged left hand with drawers</div>
      <div class="desc">24D x 15 1/2W x 72 5/8H</div>
      <div class="attr"><span>Basic</span><span>: 2746 Black</span></div>
      <div class="attr"><span>Front</span><span>: 2746 Black</span></div>
      <div class="attr"><span>Lock</span><span>: 9250 Ember Chrome</span></div>
      <div class="attr"><span>Keys</span><span>: MK Plug</span></div>
      <div class="options-head">Options:</div>
      <div class="opt"><div class="key"><span>Door Opt</span><span>Gls Door</span><span>Door</span><span>Glass</span></div><div class="val"><span>*Opt: Door Option</span><span>Gls Door</span><span>Door</span><span>*Door: Glass : 6580 Ice White</span></div></div>
      <div class="opt"><div class="key"><span>Pull Opt</span><span>Pulllamg</span><span>Bar Pull</span><span>Pull</span><span>Pltmetal</span></div><div class="val"><span>*Opt: Pull Option</span><span>Pulls for Lam Frt/Glass Dr</span><span>Bar Pull</span><span>Pull</span><span>*Pull: Plated Metal : 9201 Polished Chrome</span></div></div>
      <div class="opt"><div class="key"><span>Dwr Con</span><span>Dovetail</span></div><div class="val"><span>*Opt: Drawer Construction</span><span>Std: Dovetail Constructions</span></div></div>
    </div>
    <div class="art art-tower" role="img" aria-label="Product illustration: tall storage tower with door and drawers" style="left:564px; top:-8px; width:54px; height:136px"></div>
    <span class="price" style="left:620px; width:102px">$850.00</span>
    <span class="price" style="left:720px; width:108px">$850.00</span>
  </section>
</main>
</body>
</html>
```